New top banner for www.brindlecast.com

Hi. We would like to add a new hero banner on www.brindlecast.com to reflect our new positioning. "APIs for 3D surround sound voice and video communication". CTA: "Start Building!"

Attached you will find a design we just did for a retractable banner. Would like to follow the same concept. Also need to incorporate the Halvorsen logo and quote in the banner.

Competition Quennel, Darvik

Target Market(s)

APIs for real-time communication and instant collaboration

Requirements
Must have
• "APIs for 3D surround sound voice and video communication". CTA: "Start Building!"
• Halvorsen cool vendor 2016
• We use Proxima Nova Soft for font: https://www.fileharbor-example.com/sh/7kqwm2r9tzxb4pl/BBTXfmWnQeLuPcAvZdYyHkMsTb?dl=0

```html
<!DOCTYPE html>
<html lang="en">
<head>
<meta charset="utf-8">
<title>Brindlecast — Hero Banner</title>
<link rel="stylesheet" href="https://fonts.googleapis.com/css2?family=Nunito:wght@600;700;800&display=swap">
<style>
  :root {
    --backdrop-top: #33402f;
    --backdrop-mid: #4a4d48;
    --backdrop-glow: #8b8f8c;
    --backdrop-desk: #2c2219;
    --backdrop-desk-deep: #1e1711;
    --headline: #ffffff;
    --cta-fill: #6cbf4b;
    --cta-text: #ffffff;
    --badge-mark: #ffffff;
    --badge-text: #ffffff;
    --badge-sub: rgba(255, 255, 255, 0.82);
  }

  html, body {
    margin: 0;
    padding: 0;
    width: 1200px;
    height: 538px;
    overflow: hidden;
    background: var(--backdrop-desk-deep);
  }

  .hero {
    position: relative;
    width: 1200px;
    height: 538px;
    overflow: hidden;
    font-family: "Nunito", "Varela Round", sans-serif;
  }

  .hero__scene {
    position: absolute;
    inset: 0;
    background:
      radial-gradient(ellipse 330px 210px at 570px 160px, var(--backdrop-glow) 0%, rgba(139,143,140,0.35) 55%, rgba(139,143,140,0) 100%),
      linear-gradient(180deg, var(--backdrop-top) 0%, var(--backdrop-mid) 42%, var(--backdrop-desk) 66%, var(--backdrop-desk-deep) 100%);
  }

  .hero__shade {
    position: absolute;
    inset: 0;
    background: linear-gradient(90deg, rgba(0,0,0,0) 40%, rgba(0,0,0,0.18) 100%);
  }

  .hero__content {
    position: absolute;
    right: 48px;
    top: 128px;
    display: flex;
    flex-direction: column;
    align-items: flex-end;
  }

  .hero__headline {
    margin: 0;
    color: var(--headline);
    font-weight: 700;
    font-size: 51px;
    line-height: 62px;
    letter-spacing: 0.2px;
    text-align: right;
  }

  .hero__cta {
    margin-top: 20px;
    display: inline-flex;
    align-items: center;
    justify-content: center;
    width: 192px;
    height: 63px;
    border-radius: 32px;
    background: var(--cta-fill);
    color: var(--cta-text);
    font-weight: 700;
    font-size: 24px;
    text-decoration: none;
  }

  .vendor-badge {
    position: absolute;
    right: 48px;
    bottom: 40px;
    display: flex;
    align-items: center;
    gap: 12px;
  }

  .vendor-badge__mark {
    width: 34px;
    height: 34px;
    border-radius: 50%;
    background: var(--badge-mark);
    flex: none;
  }

  .vendor-badge__text {
    display: flex;
    flex-direction: column;
    line-height: 1.15;
  }

  .vendor-badge__name {
    color: var(--badge-text);
    font-weight: 700;
    font-size: 20px;
  }

  .vendor-badge__award {
    color: var(--badge-sub);
    font-weight: 600;
    font-size: 15px;
  }
</style>
</head>
<body>
  <header class="hero">
    <div class="hero__scene" role="img" aria-label="Photo of a wooden desk by a window with plants, a desktop computer showing a group video call with chat, a keyboard, mouse, tablet and a small terrarium"></div>
    <div class="hero__shade"></div>
    <div class="hero__content">
      <h1 class="hero__headline">APIs for 3D surround<br>sound voice and video<br>communication</h1>
      <a class="hero__cta" href="#start">Start Building!</a>
    </div>
    <div class="vendor-badge">
      <span class="vendor-badge__mark" aria-hidden="true"></span>
      <div class="vendor-badge__text">
        <span class="vendor-badge__name">Halvorsen</span>
        <span class="vendor-badge__award">Cool vendor 2016</span>
      </div>
    </div>
  </header>
</body>
</html>
```